Shotcrete Contractor Needs Business Cards Designed

We're a Shotcrete construction company based out of Southern California who opened another office in Northern California and needs new cards. The cards need to have our logo,name,title,license #,contact info, and website. Both office locations need to be on the card as well. We are looking for a professional clean design that will work well in the construction industry. PLEASE VISIT THE WEBSITE to get a feel about the company. www.harborlineshotcrete.example

Industry/Entity Type

Construction

```html
<!DOCTYPE html>
<html lang="en">
<head>
<meta charset="utf-8">
<title>Harborline Shotcrete – Business Cards</title>
<link href="https://fonts.googleapis.com/css2?family=Lato:wght@400;700;900&display=swap" rel="stylesheet">
<style>
  :root {
    --navy: #25216b;
    --red: #d0242c;
    --white: #ffffff;
    --paper-bg: #e4e5e8;
  }
  * { box-sizing: border-box; margin: 0; padding: 0; }
  html, body { width: 1200px; height: 900px; overflow: hidden; }
  body {
    background: var(--paper-bg);
    font-family: "Lato", sans-serif;
    display: flex;
    flex-direction: column;
    align-items: center;
    justify-content: center;
    gap: 36px;
  }
  .card {
    position: relative;
    width: 700px;
    height: 400px;
    background: var(--white);
    box-shadow: 0 6px 18px rgba(0,0,0,.18);
    overflow: hidden;
  }

  /* Front */
  .card-front .brand {
    position: absolute;
    inset: 0 0 14px 0;
    display: flex;
    align-items: center;
    justify-content: center;
    gap: 16px;
  }
  .brand-square { width: 26px; height: 26px; background: var(--red); }
  .brand-name {
    color: var(--navy);
    font-weight: 900;
    font-size: 40px;
    letter-spacing: 1px;
    text-transform: uppercase;
  }
  .front-stripe {
    position: absolute;
    left: 0; right: 0; bottom: 0;
    height: 14px;
    display: flex;
  }
  .front-stripe .red { flex: 0 0 43%; background: var(--red); }
  .front-stripe .navy { flex: 1; background: var(--navy); }

  /* Back */
  .card-back .brand {
    position: absolute;
    top: 30px; left: 0; right: 0;
    display: flex;
    align-items: center;
    justify-content: center;
    gap: 12px;
  }
  .card-back .brand-name { font-size: 28px; }
  .card-back .brand-square { width: 18px; height: 18px; }

  .person {
    position: absolute;
    right: 44px;
    top: 100px;
    text-align: right;
    line-height: 1.2;
  }
  .person-name { color: var(--navy); font-weight: 700; font-size: 25px; }
  .person-title, .person-license { color: var(--red); font-size: 19px; }
  .person-marker { position: absolute; right: 0; top: 106px; }

  .rule-red {
    position: absolute;
    left: 0; right: 0; top: 200px;
    height: 12px;
    background: var(--red);
  }
  .contact-band {
    position: absolute;
    left: 0; right: 0; top: 222px; bottom: 0;
    background: var(--navy);
    color: var(--white);
    display: flex;
    justify-content: space-between;
    align-items: center;
    padding: 0 32px 0 0;
  }
  .contact-list {
    list-style: none;
    font-size: 17px;
    line-height: 1.62;
  }
  .contact-list li { display: flex; align-items: center; gap: 18px; }
  .contact-list li svg { flex: none; }
  .contact-list b { font-weight: 700; font-style: italic; }

  .offices {
    position: relative;
    text-align: right;
    font-size: 15px;
    line-height: 1.45;
  }
  .office-name { font-weight: 700; letter-spacing: .4px; font-size: 16px; }
  .office + .office { margin-top: 6px; }
  .office-marker { position: absolute; right: -32px; top: 3px; }
</style>
</head>
<body>

<section class="card card-front" aria-label="Card front">
  <div class="brand">
    <span class="brand-square"></span>
    <span class="brand-name">Harborline Shotcrete</span>
  </div>
  <div class="front-stripe"><span class="red"></span><span class="navy"></span></div>
</section>

<section class="card card-back" aria-label="Card back">
  <div class="brand">
    <span class="brand-square"></span>
    <span class="brand-name">Harborline Shotcrete</span>
  </div>

  <div class="person">
    <div class="person-name">YOUR NAME</div>
    <div class="person-title">Title</div>
    <div class="person-license">License No.</div>
  </div>
  <svg class="person-marker" width="30" height="26" viewBox="0 0 30 26" aria-hidden="true">
    <polygon points="30,0 30,26 0,13" fill="var(--red)"/>
  </svg>

  <div class="rule-red"></div>

  <div class="contact-band">
    <ul class="contact-list">
      <li><svg width="22" height="20" viewBox="0 0 22 20"><polygon points="0,0 22,10 0,20" fill="var(--red)"/></svg><span><b>Fax:</b> 661-555-0192</span></li>
      <li><svg width="22" height="20" viewBox="0 0 22 20"><polygon points="0,0 22,10 0,20" fill="var(--red)"/></svg><span><b>Phone:</b> (877) 555-0148</span></li>
      <li><svg width="22" height="20" viewBox="0 0 22 20"><polygon points="0,0 22,10 0,20" fill="var(--red)"/></svg><span><b>Email:</b> info@harborlineshotcrete.example</span></li>
      <li><svg width="22" height="20" viewBox="0 0 22 20"><polygon points="0,0 22,10 0,20" fill="var(--red)"/></svg><span><b>Website:</b> www.harborlineshotcrete.example</span></li>
    </ul>
    <div class="offices">
      <div class="office-name">HARBORLINE SHOTCRETE, INC.</div>
      <div class="office">
        <div>4810 Cedar Crest Avenue, Suite 120,</div>
        <div>Valencia, CA 91355</div>
      </div>
      <div class="office">
        <div>2250 Alder Point Road, Suite 8,</div>
        <div>Sacramento, CA 95815</div>
      </div>
      <svg class="office-marker" width="20" height="18" viewBox="0 0 20 18" aria-hidden="true">
        <polygon points="20,0 20,18 0,9" fill="var(--red)"/>
      </svg>
    </div>
  </div>
</section>

</body>
</html>
```